small business website design

***Update: need the design to be coded into a wordpress or similar format***
Need a website for a small business with big plans. No online ordering etc but business description and contact details pages, a page showing products we use and page for customers or suppliers to register with us. Also want links to chirpnest. We have a logo existing but also open to any improvements on the design. We have an existing website we created and looks very DIY but you can get some info from it to help create your design for us.
Hi Everyone, we didn't make it clear at the beginning but we would like the final design to be in a coded format and ready to upload to a URL. I have to apologise and admit to my lack of knowledge of the design process.
Oil / gas and industrial plant managers.
Small Business

```html
<!DOCTYPE html>
<html lang="en">
<head>
<meta charset="utf-8">
<title>Tankline Metering Services</title>
<link href="https://fonts.googleapis.com/css2?family=Open+Sans:wght@400;600&display=swap" rel="stylesheet">
<style>
:root{
  --page:#e9f6fb;
  --blue:#2e9fd6;
  --blue-dark:#1d7fb4;
  --nav-top:#3aaee0;
  --nav-bottom:#1f8cc4;
  --ink:#555;
  --ink-soft:#777;
  --title:#333;
  --line:#cfd9de;
  --footer:#c9e2ea;
  --footer-base:#d3e8ef;
}
*{box-sizing:border-box;margin:0;padding:0}
html,body{width:679px;height:1200px;overflow:hidden}
body{background:var(--page);font-family:'Open Sans',sans-serif;color:var(--ink);position:relative}
.abs{position:absolute}

.brand-mark{left:48px;top:30px;width:72px;height:72px;border-radius:50%;background:#b8c2cc}
.brand-name{left:136px;top:34px;font-size:19px;line-height:26px;color:var(--title);font-weight:400}
.phone{right:18px;top:42px;color:var(--blue);font-size:14px;display:flex;align-items:center;gap:8px;white-space:nowrap}
.search{left:482px;top:76px;width:147px;height:21px;background:#fff;border:1px solid var(--line);font-size:8px;color:#666;padding:5px 8px;display:flex;justify-content:space-between}

.nav-band{left:0;top:117px;width:679px;height:33px;background:linear-gradient(var(--nav-top),var(--nav-bottom))}
.nav{left:49px;top:117px;width:580px;height:33px;display:flex}
.nav a{color:#fff;text-decoration:none;font-size:9px;font-weight:600;display:flex;align-items:center;justify-content:center;white-space:nowrap;border-right:1px solid rgba(255,255,255,.25)}
.nav a:last-child{border-right:0}
.nav a.active{background:rgba(0,0,0,.12)}

.hero{left:0;top:150px;width:679px;height:243px;background:linear-gradient(#bcd0e0 0%,#e4eaee 30%,#d9dee2 55%,#6a5e50 58%,#8c96a0 75%,#a9b6c2 100%)}
.hero-arrow{top:258px;width:26px;height:26px;border-radius:50%;background:rgba(80,80,80,.45)}
.caption{left:118px;top:303px;width:242px;height:63px;background:rgba(40,40,40,.45);color:#fff;padding:6px 11px}
.caption h2{font-size:12.5px;line-height:17px;font-weight:600;margin-bottom:5px;white-space:nowrap}
.caption p{font-size:7px;line-height:11px}

.tiles{left:50px;top:430px;width:578px;height:223px;display:grid;grid-template-columns:repeat(4,1fr);grid-template-rows:repeat(2,1fr)}
.tile{background:#fff;text-align:center;padding:16px 10px 0}
.tile h3{font-size:14px;font-weight:400;color:#444;padding-bottom:7px;border-bottom:1px solid #bbb;margin:0 8px 10px}
.tile p{font-size:8px;line-height:12px;color:var(--ink-soft);margin-bottom:9px}
.tile span{font-size:8.5px;color:var(--ink-soft)}
.tile.featured{background:var(--blue)}
.tile.featured h3,.tile.featured p,.tile.featured span{color:#fff;border-color:#fff}
.tile.photo{padding:0}

.welcome h2,.news h2{color:var(--blue);font-size:15px;font-weight:400;white-space:nowrap}
.welcome-img{left:50px;top:729px;width:140px;height:93px;background:linear-gradient(#3a4f7a,#c98a3a 60%,#6a5a48)}
.welcome-text{left:207px;top:727px;width:175px;font-size:8px;line-height:14px;color:var(--ink)}
.news ul{list-style:none;margin-top:12px}
.news li{font-size:8px;line-height:12px;position:relative;padding-left:16px;margin-bottom:9px;width:330px}
.news li::before{content:"";position:absolute;left:1px;top:2px;width:6px;height:6px;border:1.5px solid #666;border-radius:50%}
.more{left:354px;top:955px;font-size:8.5px;color:var(--blue)}

.form{left:439px;top:701px;width:190px;height:264px;background:#fff;border:1px solid var(--line);padding:14px 10px}
.form h3{color:var(--blue-dark);font-size:14px;font-weight:400;text-align:center;margin-bottom:13px}
.field{border:1px solid #c5cfd4;height:24px;font-size:8px;padding:6px 8px;margin-bottom:10px;color:#555}
.field.msg{height:65px}
.submit{display:block;margin:14px auto 0;width:134px;height:27px;background:var(--blue);color:#fff;font-size:11px;border:0;border-bottom:2px solid var(--blue-dark);font-family:inherit}

.footer{left:0;top:1009px;width:679px;height:150px;background:var(--footer)}
.badge-a{left:50px;top:1037px;width:104px;height:90px;background:#d8383a}
.badge-b{left:204px;top:1058px;width:206px;height:52px;background:#e7eef1;border:1px solid #aab}
.newsletter{left:476px;top:1033px;width:153px}
.newsletter h4{font-size:12px;font-weight:400;color:#555;margin-bottom:6px}
.newsletter p{font-size:8px;line-height:16px;color:#555}
.nl-input{height:20px;background:#fff;border:1px solid #b9ccd3;margin-top:8px}
.subscribe{left:560px;top:1120px;width:69px;height:21px;background:var(--blue);color:#fff;font-size:9px;display:flex;align-items:center;justify-content:center}

.base{left:0;top:1159px;width:679px;height:41px;background:var(--footer-base);border-top:1px solid #b8d2da}
.copy{left:50px;top:1175px;font-size:7.5px;color:#555}
.social{left:528px;top:1171px;display:flex;gap:5px}
.social i{width:16px;height:16px;border-radius:50%;background:#6f97b8;display:block}
</style>
</head>
<body>
<header>
  <div class="abs brand-mark" aria-hidden="true"></div>
  <div class="abs brand-name">Tankline Metering<br>Services</div>
  <div class="abs phone">+61 02 5550 1742
    <svg width="12" height="16" viewBox="0 0 12 16"><path d="M3 1 L5 5 L3.5 6.5 Q4.5 10 7 12 L8.5 10.5 L11.5 13 L9.5 15.5 Q2 13 1 3 Z" fill="var(--blue)"/></svg>
  </div>
  <div class="abs search"><span>Search..</span>
    <svg width="9" height="9" viewBox="0 0 10 10"><circle cx="4" cy="4" r="3" fill="none" stroke="#888" stroke-width="1.3"/><line x1="6.3" y1="6.3" x2="9" y2="9" stroke="#888" stroke-width="1.3"/></svg>
  </div>
</header>

<div class="abs nav-band"></div>
<nav class="abs nav">
  <a class="active" href="#" style="width:63px">HOME</a>
  <a href="#" style="width:78px">ABOUT US</a>
  <a href="#" style="width:76px">SERVICES</a>
  <a href="#" style="width:81px">PRODUCTS</a>
  <a href="#" style="width:105px">NEWS &amp; EVENTS</a>
  <a href="#" style="width:97px">TESTIMONIALS</a>
  <a href="#" style="width:80px">CONTACT</a>
</nav>

<section class="abs hero" role="img" aria-label="Row of white fuel storage tanks at a waterfront terminal reflected in the water"></section>
<div class="abs hero-arrow" style="left:48px"><svg width="26" height="26"><path d="M15 8 L10 13 L15 18" stroke="#fff" fill="none" stroke-width="1.2"/></svg></div>
<div class="abs hero-arrow" style="left:604px"><svg width="26" height="26"><path d="M11 8 L16 13 L11 18" stroke="#fff" fill="none" stroke-width="1.2"/></svg></div>
<div class="abs caption">
  <h2>Consectetuer adipisc ing elitraesent</h2>
  <p>Claritas est etiam processus dynamicus, qui sequitur mutationem consuetudium lectorum. Mirum est notare equitur.</p>
</div>

<section class="abs tiles">
  <div class="tile photo" role="img" aria-label="Yellow wheel loader moving earth" style="background:linear-gradient(#d8dde2,#c9852f 50%,#8a4a28)"></div>
  <div class="tile featured"><h3>Project Support</h3><p>Maseleme leifendeuctor wisnes nera iliquam eratutpas rutrem.</p><span>Read More</span></div>
  <div class="tile photo" role="img" aria-label="Site worker in a hard hat at an industrial facility" style="background:linear-gradient(#8a9aa8,#d9b34a 40%,#5a6470)"></div>
  <div class="tile"><h3>Services</h3><p>Maseleme leifendeuctor wisnes nera iliquam eratutpas rutrem.</p><span>Read More</span></div>
  <div class="tile"><h3>Our Capablities</h3><p>Maseleme leifendeuctor wisnes nera iliquam eratutpas rutrem.</p><span>Read More</span></div>
  <div class="tile photo" role="img" aria-label="Steel pipework at a processing plant" style="background:linear-gradient(135deg,#9aa4ae,#d6dbe0 45%,#5c6670)"></div>
  <div class="tile"><h3>Products</h3><p>Maseleme leifendeuctor wisnes nera iliquam eratutpas rutrem.</p><span>Read More</span></div>
  <div class="tile photo" role="img" aria-label="Close view of machine gears" style="background:radial-gradient(circle at 60% 50%,#9fb0c0,#2b3440 75%)"></div>
</section>

<section class="welcome">
  <h2 class="abs" style="left:50px;top:696px">Welcome to Tankline Metering Services</h2>
  <div class="abs welcome-img" role="img" aria-label="Overhead crane inside an industrial workshop"></div>
  <p class="abs welcome-text">Duis autem vel euim iriure dolor in hendrerit vulputate velit esse molestie consequat, vnllu m dolore eu feugiat nulla facilisis at vero eros accumsan et iusto odio dignissim qui blandpr aesent luptatum zzril delenit augue duisolore te feugait nulla facilisi. Nam liber tempor cum oluta nobis eleifend option congue.</p>
</section>

<section class="abs news" style="left:50px;top:842px">
  <h2>Latest News</h2>
  <ul>
    <li>Established in 1986 with 25 years of outstanding service, a state approved vendor</li>
    <li>A Service-Disabled Veteran-Owned company focused on hiring Service Disablietera ns, Veterans and family members of veterans</li>
    <li>As a member of the Regional Green Building Network support green design, construction and operations</li>
  </ul>
</section>
<a class="abs more">More..</a>

<form class="abs form">
  <h3>Contact Form</h3>
  <div class="field">Name</div>
  <div class="field">Phone</div>
  <div class="field">E-mail</div>
  <div class="field msg">Message</div>
  <button class="submit" type="button">Submit Request</button>
</form>

<footer>
  <div class="abs footer"></div>
  <div class="abs badge-a" aria-hidden="true"></div>
  <div class="abs badge-b" aria-hidden="true"></div>
  <div class="abs newsletter">
    <h4>Newsletter</h4>
    <p>Stay in touch with us by signing up for our quarterly newsletter!</p>
    <div class="nl-input"></div>
  </div>
  <div class="abs subscribe">SUBSCRIBE</div>
  <div class="abs base"></div>
  <div class="abs copy">Copyright ©2013. All Rights Reserved.</div>
  <div class="abs social" aria-label="chirpnest and other social links"><i></i><i></i><i></i><i></i></div>
</footer>
</body>
</html>
```